Vantorix Business
Card and Letter Head
Creative Brief
Professional
Dalton Prewitt
Owner
7153 Hollow Creek Christiansted, Ferrin Isle VX 00471
sales@vantorix.net
vantorix.net
Custom Integrator
ultimate digital experience

```html
<!DOCTYPE html>
<html lang="en">
<head>
<meta charset="utf-8">
<title>Vantorix Business Card</title>
<link href="https://fonts.googleapis.com/css2?family=Montserrat:wght@400;600;700&display=swap" rel="stylesheet">
<style>
  :root {
    --page: #ffffff;
    --dark-1: #4a4744;
    --dark-2: #2c2a28;
    --dark-3: #1f1d1c;
    --cream: #f8f5e1;
    --ink: #6a6560;
    --ink-soft: #8a847c;
    --white: #f4f1ea;
    --mark: #c9bfa6;
  }
  * { margin: 0; padding: 0; box-sizing: border-box; }
  html, body {
    width: 1200px; height: 334px; overflow: hidden;
    background: var(--page);
    font-family: "Montserrat", Arial, sans-serif;
  }
  .sheet { position: relative; width: 1200px; height: 334px; }
  .card {
    position: absolute; top: 5px; height: 321px;
    overflow: hidden;
    box-shadow: 0 1px 3px rgba(0,0,0,.25);
  }
  .card--front { left: 0; width: 557px; background: var(--cream); }
  .card--back {
    left: 629px; width: 571px;
    background: linear-gradient(120deg, var(--dark-1), var(--dark-2) 55%, var(--dark-3));
  }
  .front-band {
    position: absolute; left: 0; top: 0; width: 100%; height: 188px;
    background: linear-gradient(120deg, var(--dark-1), var(--dark-2) 55%, var(--dark-3));
  }
  .emblem-wash {
    position: absolute; top: 0; right: 0; width: 320px; height: 100%;
    background: radial-gradient(ellipse at 55% 45%, rgba(255,255,255,.09), rgba(255,255,255,0) 68%);
  }
  .card--front .emblem-wash { height: 188px; width: 300px; }
  .brand { position: absolute; display: flex; flex-direction: column; align-items: center; }
  .brand-dot {
    width: 50px; height: 50px; border-radius: 50%;
    border: 2px solid var(--mark);
  }
  .brand-name {
    color: var(--white); font-weight: 400; letter-spacing: 1.5px; text-transform: uppercase;
  }
  .card--front .brand { left: 14px; top: 16px; align-items: center; }
  .card--front .brand-dot { margin-bottom: 44px; }
  .card--front .brand-name { font-size: 22px; }
  .card--back .brand { left: 14px; width: 160px; top: 84px; }
  .card--back .brand-dot { width: 64px; height: 64px; margin-bottom: 36px; }
  .card--back .brand-name { font-size: 22px; }
  .holder { position: absolute; top: 220px; width: 100%; text-align: center; color: var(--ink); }
  .holder-name { font-size: 19px; font-weight: 700; letter-spacing: 1.2px; text-transform: uppercase; line-height: 22px; }
  .holder-role { font-size: 11px; font-weight: 600; letter-spacing: 1px; text-transform: uppercase; line-height: 14px; }
  .contact {
    position: absolute; left: 0; width: 100%; top: 276px; text-align: center;
    font-size: 9px; color: var(--ink-soft); line-height: 18px; letter-spacing: .2px;
  }
  .contact b { font-weight: 700; color: var(--ink); text-transform: uppercase; }
</style>
</head>
<body>
<div class="sheet">
  <section class="card card--front">
    <div class="front-band"></div>
    <div class="emblem-wash" role="img" aria-label="Faint large lion head decoration"></div>
    <div class="brand">
      <span class="brand-dot"></span>
      <span class="brand-name">Vantorix</span>
    </div>
    <div class="holder">
      <div class="holder-name">Dalton Prewitt</div>
      <div class="holder-role">Owner</div>
    </div>
    <div class="contact">
      <div><b>Add :</b> 7153 Hollow Creek Harborvale, Ferrin Isle VX 00471</div>
      <div><b>Ph :</b> 555 210 4473 <b>Fax :</b> 555 210 4488 <b>Email :</b> sales@vantorix.net <b>Web :</b> vantorix.net</div>
    </div>
  </section>
  <section class="card card--back">
    <div class="emblem-wash" role="img" aria-label="Faint large lion head decoration"></div>
    <div class="brand">
      <span class="brand-dot"></span>
      <span class="brand-name">Vantorix</span>
    </div>
  </section>
</div>
</body>
</html>
```